Elegant and modern Wedding Photography brochure

My existing brochure (attached) needs a major facelift. This is one of the main selling tools - it gets emailed to my clients when they make an equiry on what packages i offer and it is printed out and walked through at our first meeting. This brochure is as critical as my website - it needs to sing!

I'm looking for an eye-catching design that says:
Elegant
Modern
Clean
Crisp
Not cutesy or lovey-dovey thanks - we are more sophisticated and professional than that.

Update images to some of the latest weddings I've shot also. Let me know files and resolution you need. I've enabled right-click to download images on my site for a limited time. Please note that I retain copyright and will pursue any breeches.

Http://www.carlathornbey.com/Melbourne-wedding-photography
Updates

Thanks for all of your designs! Will take a few days to decide.

Target Market(s)

Australian Women aged 24-44

Industry/Entity Type

Wedding

Font styles to use
Other font styles liked:
• Century Gothic

Requirements
Must have
• Easy to print - does not have to be 6 A4 pages like the existing brochure
Nice to have
• Some full page images - The photos are supposed to be the hero here :-)
Should not have
• Not cutesy or lovey-dovey thanks - we are more sophisticated and professional than that.

No black backgrounds, I prefer a white thanks

No images in organic shaped boxes (like the rectangles in the logo - no thanks).
Keep the lines straight and sharp

```html
<!DOCTYPE html>
<html lang="en">
<head>
<meta charset="utf-8">
<title>Carla Thornbey — À la Carte Fees</title>
<link rel="stylesheet" href="https://fonts.googleapis.com/css2?family=Didact+Gothic&family=Roboto+Slab:wght@300&display=swap">
<style>
  :root {
    --purple: #8e2a8c;
    --purple-deep: #7a1f80;
    --purple-bright: #dd7cf0;
    --purple-pale: #f3d8f4;
    --story-pink: #ecc9ec;
    --tagline-grey: #dddddd;
    --text-grey: #9a9a9a;
    --icon-grey: #3e3e3e;
    --white: #ffffff;
  }
  * { margin: 0; padding: 0; box-sizing: border-box; }
  html, body { width: 1200px; height: 900px; overflow: hidden; background: var(--white); }
  .sheet { position: relative; width: 1200px; height: 900px; font-family: "Roboto Slab", serif; }

  .tagline { position: absolute; top: 28px; font-family: "Didact Gothic", sans-serif; font-size: 40px; line-height: 48px; white-space: nowrap; }
  .tagline--story { left: 113px; color: var(--story-pink); }
  .tagline--photographer { left: 810px; color: var(--tagline-grey); letter-spacing: 0.6px; }

  .brand { position: absolute; left: 398px; top: 18px; display: flex; align-items: center; gap: 14px; }
  .brand__square { width: 62px; height: 58px; border: 3px solid var(--purple); flex: none; }
  .brand__name { font-family: "Didact Gothic", sans-serif; font-size: 42px; line-height: 58px; color: var(--purple); white-space: nowrap; }
  .subtitle { position: absolute; left: 492px; top: 80px; font-family: "Didact Gothic", sans-serif; font-size: 21px; line-height: 22px; font-weight: 400; color: var(--purple); white-space: nowrap; }

  .band { position: absolute; left: 0; top: 105px; width: 1200px; height: 62px; }
  .band__rule-top { position: absolute; left: 0; top: 0; width: 100%; height: 4px; background: var(--purple-deep); }
  .band__stripe { position: absolute; left: 0; top: 13px; width: 100%; height: 36px;
    background: linear-gradient(90deg, #b04ec4 0%, #a23bb8 18%, #f2d6f5 36%, #c066d4 52%, #a53cb9 62%, var(--purple-bright) 78%, #9a2fb0 92%, #8a2aa0 100%); }
  .band__rule-bottom { position: absolute; left: 0; top: 52px; width: 100%; height: 10px;
    background: linear-gradient(180deg, var(--purple-pale) 0%, var(--purple-deep) 60%, #9a4aa0 100%); }

  .photo { position: absolute; }
  .photo--couple-wall { left: 21px; top: 191px; width: 397px; height: 262px; background: radial-gradient(ellipse at 40% 55%, #8a8a8a, #2a2a2a 80%); }
  .photo--couple-stone { left: 449px; top: 194px; width: 188px; height: 120px; background: linear-gradient(135deg, #3d5e6a, #8aa2a0 60%, #3a4d55); }
  .photo--couple-trees { left: 449px; top: 330px; width: 187px; height: 124px; background: linear-gradient(135deg, #5a5530, #a39470 55%, #3b3720); }
  .photo--couple-shed { left: 26px; top: 465px; width: 230px; height: 151px; background: linear-gradient(135deg, #6b4c34, #b89a82 55%, #5a4535); }
  .photo--couple-avenue { left: 276px; top: 466px; width: 360px; height: 234px; background: linear-gradient(120deg, #5b6a52, #a1a58f 50%, #2f3a2c); }
  .photo--dahlia { left: 25px; top: 635px; width: 229px; height: 220px; background: radial-gradient(circle at 40% 40%, #b0637a, #c9a596 55%, #d7c4b4); }
  .photo--clocktower { left: 277px; top: 715px; width: 218px; height: 140px; background: linear-gradient(180deg, #e8e8e8, #8a8a8a 55%, #3a3a3a); }
  .photo--couple-kiss { left: 510px; top: 715px; width: 126px; height: 142px; background: linear-gradient(135deg, #cfcfcf, #5a5a5a 60%, #2a2a2a); }

  .fees { position: absolute; left: 674px; top: 188px; width: 515px; list-style: none; font-size: 16px; line-height: 21px; color: var(--text-grey); font-weight: 300; }
  .fee { position: absolute; left: 0; width: 515px; }
  .fee__name { color: var(--purple); }
  .fee__name--italic { font-style: italic; }
  .fee__detail { font-style: italic; }

  .social { position: absolute; top: 860px; left: 967px; display: flex; gap: 23px; }
  .social__dot { width: 26px; height: 26px; border-radius: 50%; background: var(--icon-grey); }
</style>
</head>
<body>
<main class="sheet">
  <header>
    <div class="tagline tagline--story">Your Story.</div>
    <div class="brand">
      <span class="brand__square"></span>
      <span class="brand__name">Carla Thornbey</span>
    </div>
    <div class="tagline tagline--photographer">Your Photographer.</div>
    <h1 class="subtitle">À la Carte Fees to Consider</h1>
  </header>

  <div class="band">
    <div class="band__rule-top"></div>
    <div class="band__stripe"></div>
    <div class="band__rule-bottom"></div>
  </div>

  <section class="gallery">
    <div class="photo photo--couple-wall" role="img" aria-label="Black and white portrait of an engaged couple against a dark wall"></div>
    <div class="photo photo--couple-stone" role="img" aria-label="Couple embracing beside a stone wall"></div>
    <div class="photo photo--couple-trees" role="img" aria-label="Couple kissing among trees in warm light"></div>
    <div class="photo photo--couple-shed" role="img" aria-label="Couple smiling by a timber shed"></div>
    <div class="photo photo--couple-avenue" role="img" aria-label="Couple posing in a tree-lined avenue"></div>
    <div class="photo photo--dahlia" role="img" aria-label="Pink dahlia buttonhole on a wooden surface"></div>
    <div class="photo photo--clocktower" role="img" aria-label="Couple walking toward a clock tower, black and white"></div>
    <div class="photo photo--couple-kiss" role="img" aria-label="Couple kissing, black and white"></div>
  </section>

  <ul class="fees">
    <li class="fee" style="top:0"><span class="fee__name">Engagement Session/Pre-wedding Shoot</span> <span class="fee__detail">- $290 for up to<br>2 hours of photography on location</span></li>
    <li class="fee" style="top:63px"><span class="fee__name">Digital Negatives</span> <span class="fee__detail">- $490</span></li>
    <li class="fee" style="top:106px"><span class="fee__name">Extended Coverage</span> <span class="fee__detail">- $160 per hour</span></li>
    <li class="fee" style="top:148px"><span class="fee__name fee__name--italic">Web Gallery &amp; Friendwall posting</span> <span class="fee__detail">- $160</span></li>
    <li class="fee" style="top:190px"><span class="fee__name fee__name--italic">Slideshow</span> <span class="fee__detail">- $250</span></li>
    <li class="fee" style="top:233px"><span class="fee__name">Second Photographer</span> <span class="fee__detail">- $590</span></li>
    <li class="fee" style="top:275px"><span class="fee__name fee__name--italic">Client for life</span> <span class="fee__detail">- $390 which includes: No sitting fees for portrait<br>sessions – Anniversaries, family portraits, etc.</span></li>
    <li class="fee" style="top:339px"><span class="fee__name">Photo Enlargements</span><br><span class="fee__detail">Quality custom archival prints in a variety of sizes 5x7 up to<br>8x10 $25, 12.5x18.5 $50 Stretched Canvas Prints for your wall<br>Various sizes available from 16"x20" starting at $395 through<br>to 60"x96" $1500. Plus many other options!</span></li>
    <li class="fee" style="top:466px"><span class="fee__name">Professionally Edited Album (Regular)</span> <span class="fee__detail">- $790</span></li>
    <li class="fee" style="top:508px"><span class="fee__name">Album Upgrade from Regular to Signature Grand</span><br><span class="fee__detail">From Gold Package to Signature Grand: $1150<br>From Platinum Package to Signature Grand: $650</span></li>
    <li class="fee" style="top:592px"><span class="fee__name fee__name--italic">Custom Thank-you Cards</span> <span class="fee__detail">- $150 for 50 cards (174mm x 123mm)<br>including envelopes</span></li>
  </ul>

  <nav class="social" aria-label="Social links">
    <span class="social__dot"></span>
    <span class="social__dot"></span>
    <span class="social__dot"></span>
    <span class="social__dot"></span>
    <span class="social__dot"></span>
  </nav>
</main>
</body>
</html>
```